Stonelynk Business Card Design

The Stonelynk Co is an aggregate (crushing) equipment dealer serving Western Canadian provinces. Stonelynk is a distributor of aggregate equipment for different manufacturers.

We are looking to change and update the existing business card which has been used since the existence of the company. A copy of existing card has been attached for reference. The Stonelynk Co logo we want to remain the same and we want the green color to remain the same.

We are wanting something new with a different look. A refreshing card to show a new modern and updated look. No longer wanting to have the manufacturers on the back of the card but something more like our logo on the back of the card with a statement like "Crushing Solutions"

ideas could be:
- card can be different colors on front and back
- front or reverse of the card could possibly be the green color with the logo in black

Target Market(s)

Owners of Aggregate/Crushing companies

Requirements
Must have
• - logo to remain same along with same font within logo
• - green color to remain same
Nice to have
• as noted above under project description
Should not have

```html
<!DOCTYPE html>
<html lang="en">
<head>
<meta charset="utf-8">
<title>The Stonelynk Co — Business Card</title>
<link href="https://fonts.googleapis.com/css2?family=Roboto+Condensed:wght@400;700&display=swap" rel="stylesheet">
<style>
  :root {
    --green: #a4b51c;
    --charcoal: #2a2b2d;
    --paper: #f1f1ef;
    --white: #ffffff;
    --stage: #e4e2dd;
    --ink-light: #f4f4f2;
    --ink-dark: #2a2b2d;
    --line: #a4b51c;
  }
  * { box-sizing: border-box; margin: 0; padding: 0; }
  html, body { width: 1200px; height: 780px; overflow: hidden; }
  body {
    background: var(--stage);
    font-family: "Roboto Condensed", Arial, sans-serif;
    display: flex; flex-direction: column; align-items: center; justify-content: center; gap: 40px;
  }
  .card {
    position: relative; width: 600px; height: 343px; overflow: hidden;
    box-shadow: 0 4px 14px rgba(0,0,0,.18);
  }

  /* Front */
  .card--front { background: var(--charcoal); color: var(--ink-light); }
  .front__title {
    position: absolute; left: 0; top: 0; width: 100%; height: 68px;
    border-bottom: 2px solid var(--line);
    font-weight: 700; font-size: 40px; letter-spacing: .5px; line-height: 66px; padding-left: 172px;
    white-space: nowrap;
  }
  .front__logo {
    position: absolute; left: 0; top: 68px; width: 156px; height: 146px;
    background: var(--white); display: flex; align-items: center; justify-content: center; gap: 8px;
  }
  .front__logo-dot { width: 16px; height: 16px; border-radius: 50%; background: var(--green); }
  .front__logo-name { color: var(--green); font-weight: 700; font-size: 20px; white-space: nowrap; }
  .front__fax {
    position: absolute; left: 0; top: 214px; width: 156px; height: 44px;
    border-top: 2px solid var(--line); font-size: 17px; line-height: 42px; padding-left: 14px; white-space: nowrap;
  }
  .front__row {
    position: absolute; left: 156px; height: 48px; border-left: 2px solid var(--line);
    border-bottom: 2px solid var(--line); font-size: 17px; line-height: 46px; padding-left: 14px; white-space: nowrap;
  }
  .front__name { top: 68px; width: 150px; font-weight: 700; }
  .front__direct { top: 68px; left: 306px; width: 294px; }
  .front__tel { top: 116px; width: 150px; }
  .front__email { top: 116px; left: 306px; width: 148px; font-size: 15px; }
  .front__services {
    position: absolute; left: 454px; top: 116px; width: 146px; height: 98px;
    border-left: 2px solid var(--line); border-bottom: 2px solid var(--line);
    padding: 10px 0 0 14px; list-style: none;
  }
  .front__services li { font-size: 16px; letter-spacing: 2px; line-height: 26px; display: flex; align-items: center; gap: 8px; }
  .front__services li::before { content: ""; width: 10px; height: 10px; border-radius: 50%; background: var(--green); }
  .front__panel {
    position: absolute; left: 156px; top: 164px; width: 298px; height: 94px; background: var(--white);
  }
  .front__social {
    position: absolute; left: 454px; top: 214px; width: 146px; height: 44px;
    display: flex; align-items: center; gap: 6px; padding-left: 14px;
  }
  .front__social span { width: 22px; height: 22px; border-radius: 50%; background: var(--green); }
  .front__address {
    position: absolute; left: 0; top: 258px; width: 100%; height: 40px;
    border-top: 2px solid var(--line); font-size: 17px; line-height: 38px; padding-left: 172px; letter-spacing: .3px;
  }
  .front__web {
    position: absolute; left: 0; bottom: 0; width: 100%; height: 45px; background: var(--green);
    color: var(--ink-dark); font-weight: 700; font-size: 22px; letter-spacing: 1.5px; line-height: 45px; padding-left: 172px;
  }

  /* Back */
  .card--back { background: linear-gradient(160deg, var(--white), var(--paper)); color: var(--ink-dark); }
  .back__title {
    position: absolute; left: 0; top: 22px; height: 56px; width: 430px; background: var(--green);
    border-radius: 0 28px 28px 0; color: var(--white); font-weight: 700; font-size: 34px;
    line-height: 56px; padding-left: 30px; white-space: nowrap;
  }
  .back__brand {
    position: absolute; left: 30px; top: 112px; display: flex; align-items: center; gap: 12px;
  }
  .back__brand-dot { width: 28px; height: 28px; border-radius: 50%; background: var(--green); }
  .back__brand-name { color: var(--green); font-weight: 700; font-size: 40px; line-height: 1; }
  .back__bar { position: absolute; left: 0; top: 224px; width: 540px; height: 16px; background: var(--charcoal); }
  .back__statement {
    position: absolute; left: 30px; top: 262px; font-weight: 700; font-size: 30px; letter-spacing: 4px;
    color: var(--ink-dark); white-space: nowrap;
  }
  .back__web {
    position: absolute; right: 0; top: 0; width: 60px; height: 100%; background: var(--green);
    display: flex; align-items: center; justify-content: center;
  }
  .back__web span {
    writing-mode: vertical-rl; transform: rotate(180deg); font-weight: 700; font-size: 18px; letter-spacing: 3px;
    white-space: nowrap;
  }
</style>
</head>
<body>
  <section class="card card--front">
    <div class="front__title">THE STONELYNK CO.</div>
    <div class="front__logo"><span class="front__logo-dot"></span><span class="front__logo-name">Stonelynk Co</span></div>
    <div class="front__fax">FAX: 780-555-0196</div>
    <div class="front__row front__name">DALE MORROW</div>
    <div class="front__row front__direct">DIRECT: 780-555-0148</div>
    <div class="front__row front__tel">TEL: 780-555-0172</div>
    <div class="front__row front__email">dale@stonelynk.com</div>
    <ul class="front__services">
      <li>SCREENERS</li>
      <li>CRUSHERS</li>
      <li>STACKERS</li>
    </ul>
    <div class="front__panel"></div>
    <div class="front__social" aria-label="Social links"><span></span><span></span><span></span><span></span></div>
    <div class="front__address">2210 48B AVE RIDGEWAY, AB &nbsp;T0X 1A1</div>
    <div class="front__web">WWW.STONELYNK.CA</div>
  </section>

  <section class="card card--back">
    <div class="back__title">THE STONELYNK CO.</div>
    <div class="back__brand"><span class="back__brand-dot"></span><span class="back__brand-name">Stonelynk Co</span></div>
    <div class="back__bar"></div>
    <div class="back__statement">CRUSHING SOLUTIONS</div>
    <div class="back__web"><span>WWW.STONELYNK.CA</span></div>
  </section>
</body>
</html>
```